Verostel business card

Business card for sustainable investment company called "Verostel". Verostel is an exchange platform selling carbon credits between buyers and sellers. Carbon Credits are an environmental commodity for reducing global carbon emissions.

the card should obviously have our logo and the theme should be sustainability/environment mixed with a trading platform.

Contact Information for Business Card

Logo, Name, Title, Phone, Email

Colors
0054AA
0677BA
7BADD7
CADEEF
E8F1F8
0094D4
00A9DD
6FCCEA
C7EBF8
E9F6FB
00AB8E
00BBA5
67D7C9
C6EFE9
E9F9F6
59FF00
82FF00
B8FF75
E3FFCB
F4FFEA

```html
<!DOCTYPE html>
<html lang="en">
<head>
<meta charset="utf-8">
<title>Verostel business card</title>
<link rel="stylesheet" href="https://fonts.googleapis.com/css2?family=Montserrat:wght@400;700&display=swap">
<style>
  :root {
    --stage: #9c9c9c;
    --card-white: #ffffff;
    --navy: #1c2b4a;
    --navy-deep: #0c1a38;
    --navy-mid: #1a3363;
    --navy-light: #2f4f8c;
    --ocean-teal: #0677ba;
    --brand-blue: #0094d4;
    --brand-cyan: #00a9dd;
    --leaf-teal: #00bba5;
    --text-grey: #555b66;
    --rule: #2a3446;
  }
  * { margin: 0; padding: 0; box-sizing: border-box; }
  html, body {
    width: 1200px;
    height: 588px;
    overflow: hidden;
    background: var(--stage);
    font-family: "Montserrat", Arial, sans-serif;
  }
  .canvas {
    position: relative;
    width: 1200px;
    height: 588px;
  }
  .card {
    position: absolute;
    top: 142px;
    width: 487px;
    height: 287px;
    border-radius: 28px;
    overflow: hidden;
  }

  /* back side */
  .card-back {
    left: 88px;
    background: linear-gradient(135deg, var(--navy-deep) 0%, var(--navy-mid) 48%, var(--navy-light) 82%, var(--ocean-teal) 100%);
  }
  .back-pattern {
    position: absolute;
    inset: 0;
    background:
      radial-gradient(circle at 80% 80%, rgba(0, 187, 165, 0.22) 0%, rgba(0, 187, 165, 0) 45%),
      radial-gradient(circle at 15% 20%, rgba(0, 0, 0, 0.25) 0%, rgba(0, 0, 0, 0) 55%);
  }
  .back-brand {
    position: absolute;
    right: 64px;
    top: 199px;
    display: flex;
    align-items: center;
    gap: 14px;
  }
  .back-brand-name {
    font-size: 24px;
    font-weight: 700;
    color: var(--card-white);
    letter-spacing: 0.5px;
  }
  .back-brand-square {
    width: 40px;
    height: 40px;
    background: var(--brand-cyan);
  }

  /* front side */
  .card-front {
    left: 622px;
    background: var(--card-white);
  }
  .brand {
    position: absolute;
    left: 24px;
    top: 27px;
    display: flex;
    align-items: center;
    gap: 24px;
  }
  .brand-square {
    width: 42px;
    height: 42px;
    background: var(--brand-blue);
  }
  .brand-name {
    font-size: 30px;
    font-weight: 700;
    color: var(--navy);
  }
  .person {
    position: absolute;
    right: 23px;
    top: 144px;
    text-align: right;
  }
  .person-name {
    font-size: 17px;
    font-weight: 700;
    color: var(--navy);
    line-height: 1.1;
  }
  .person-title {
    font-size: 13px;
    font-weight: 400;
    color: var(--text-grey);
    margin-top: 5px;
  }
  .divider {
    position: absolute;
    left: 24px;
    right: 23px;
    top: 194px;
    height: 1px;
    background: var(--rule);
  }
  .contacts {
    position: absolute;
    left: 24px;
    top: 207px;
    list-style: none;
  }
  .contacts li {
    display: flex;
    align-items: center;
    gap: 6px;
    font-size: 13.5px;
    color: var(--text-grey);
    height: 18.5px;
  }
  .contacts svg {
    width: 11px;
    height: 11px;
    flex: none;
  }
</style>
</head>
<body>
<main class="canvas">
  <section class="card card-back">
    <div class="back-pattern" role="img" aria-label="Repeating tonal pattern of the Verostel brand mark on a deep navy field"></div>
    <div class="back-brand">
      <span class="back-brand-name">VEROSTEL</span>
      <span class="back-brand-square"></span>
    </div>
  </section>

  <section class="card card-front">
    <div class="brand">
      <span class="brand-square"></span>
      <span class="brand-name">VEROSTEL</span>
    </div>

    <div class="person">
      <p class="person-name">MARCUS DELANE</p>
      <p class="person-title">President</p>
    </div>

    <div class="divider"></div>

    <ul class="contacts">
      <li>
        <svg viewBox="0 0 24 24" aria-hidden="true"><path fill="#1e88c9" d="M6.6 10.8a15.1 15.1 0 0 0 6.6 6.6l2.2-2.2a1 1 0 0 1 1-.25 11.4 11.4 0 0 0 3.6.57 1 1 0 0 1 1 1V20a1 1 0 0 1-1 1A17 17 0 0 1 3 4a1 1 0 0 1 1-1h3.5a1 1 0 0 1 1 1c0 1.25.2 2.45.57 3.57a1 1 0 0 1-.25 1z"/></svg>
        949-555-0187
      </li>
      <li>
        <svg viewBox="0 0 24 24" aria-hidden="true"><path fill="#1e88c9" d="M2 5h20v14H2z"/><path fill="none" stroke="#fff" stroke-width="2" d="M2 6l10 7 10-7"/></svg>
        marcus@verostel.com
      </li>
      <li>
        <svg viewBox="0 0 24 24" aria-hidden="true"><circle cx="12" cy="12" r="10" fill="#1e88c9"/><path fill="none" stroke="#fff" stroke-width="1.5" d="M2 12h20M12 2c3 3 3 17 0 20M12 2c-3 3-3 17 0 20"/></svg>
        www.verostel.com
      </li>
    </ul>
  </section>
</main>
</body>
</html>
```